Marlowe Holdings LLC - Business Cards

Need the following information on the cards:

Name: Dean R Vossler
Title: Chief Executive Manager

Business address:
412 N Ridgeview Lane #118
Carol Stream, Il 60412

Phone: (630) 555-0148 - Business
KPV FFL license number: 5-21-xxx-xx-xx-04519
Email: dean.vossler@marloweholdingsffl.com

Target Market(s)

Firearm owners

Industry/Entity Type

Firearms industry,

Contact Information for Business Card

Contact number, name and title, web page address, email, business address and kpv license number,

Requirements
Must have
• Name, title, business address, phone numbers, KPV license numbers, web page address and email address.
Nice to have
• Cellphone number,

```html
<!DOCTYPE html>
<html lang="en">
<head>
<meta charset="utf-8">
<title>Marlowe Holdings LLC – Business Cards</title>
<link href="https://fonts.googleapis.com/css2?family=Arimo:wght@400;700&display=swap" rel="stylesheet">
<style>
  :root{
    --stage:#e6e6e6;
    --paper-top:#d9d9d9;
    --paper-bottom:#ffffff;
    --ink:#1e1e1e;
    --red:#b5121b;
    --charcoal:#2b2b2b;
    --charcoal-deep:#1c1c1c;
  }
  *{margin:0;padding:0;box-sizing:border-box}
  html,body{width:1200px;height:900px;overflow:hidden}
  body{background:var(--stage);font-family:"Arimo",Arial,sans-serif;position:relative}

  .card{position:absolute;width:700px;height:400px;overflow:hidden;box-shadow:0 10px 24px rgba(0,0,0,.25)}
  .card::after{content:"";position:absolute;left:0;right:0;bottom:0;height:5px;background:var(--red)}

  /* front */
  .card-front{left:70px;top:30px;background:linear-gradient(160deg,var(--paper-top) 0%,#f1f1f1 45%,var(--paper-bottom) 100%)}
  .ghost-mark{position:absolute;left:20px;top:150px;width:560px;height:230px;border-radius:50% 50% 20% 20%;
    background:radial-gradient(ellipse at center,rgba(200,200,200,.35),rgba(200,200,200,0) 70%)}
  .brand-badge{position:absolute;right:60px;top:22px;width:220px;height:170px;display:flex;flex-direction:column;align-items:center;justify-content:center;gap:10px}
  .brand-badge .ring{width:86px;height:86px;border-radius:50%;border:3px solid var(--ink)}
  .brand-badge .name{font-weight:700;font-size:21px;color:var(--red);letter-spacing:1px;text-align:center;line-height:1.1}
  .address{position:absolute;right:60px;top:205px;text-align:right;font-size:18px;color:var(--ink);line-height:1.35;font-style:normal}
  .person{position:absolute;left:60px;top:150px}
  .person .name{font-weight:700;font-size:27px;color:var(--red);letter-spacing:.5px;text-transform:uppercase}
  .person .title{font-size:20px;color:var(--ink);margin-top:4px}
  .contacts{position:absolute;left:60px;top:240px;list-style:none}
  .contacts li{display:flex;align-items:center;gap:12px;font-size:19px;color:var(--ink);line-height:1.5}
  .contacts svg{width:17px;height:17px;flex:none}
  .edge-tab{position:absolute;left:0;bottom:5px;width:40px;height:22px;background:var(--red)}

  /* back */
  .card-back{left:430px;top:470px;background:linear-gradient(135deg,var(--charcoal) 0%,var(--charcoal-deep) 100%)}
  .arms-art{position:absolute;right:0;top:0;width:400px;height:395px;
    background:radial-gradient(ellipse at 55% 50%,#3a3a3a 0%,#262626 55%,rgba(30,30,30,0) 80%)}
  .back-brand{position:absolute;left:55px;top:135px;display:flex;align-items:center;gap:16px}
  .back-brand .dot{width:18px;height:18px;border-radius:50%;background:var(--red)}
  .back-brand .name{font-weight:700;font-size:40px;color:var(--red);letter-spacing:2px;line-height:1.15;text-transform:uppercase}
</style>
</head>
<body>

<section class="card card-front">
  <div class="ghost-mark" role="img" aria-label="Faint large decorative emblem artwork"></div>

  <div class="brand-badge">
    <div class="ring"></div>
    <div class="name">MARLOWE HOLDINGS LLC</div>
  </div>

  <address class="address">412 N Ridgeview Lane #118<br>Carol Stream, IL 60412</address>

  <div class="person">
    <p class="name">Dean R Vossler</p>
    <p class="title">Chief Executive Manager</p>
  </div>

  <ul class="contacts">
    <li>
      <svg viewBox="0 0 24 24" aria-hidden="true"><path fill="#b5121b" d="M6.6 10.8a15 15 0 0 0 6.6 6.6l2.2-2.2a1 1 0 0 1 1-.25 11 11 0 0 0 3.6.6 1 1 0 0 1 1 1V20a1 1 0 0 1-1 1A17 17 0 0 1 3 4a1 1 0 0 1 1-1h3.5a1 1 0 0 1 1 1c0 1.25.2 2.45.6 3.6a1 1 0 0 1-.25 1z"/></svg>
      (630) 555-0148
    </li>
    <li>
      <svg viewBox="0 0 24 24" aria-hidden="true"><rect x="2" y="5" width="20" height="14" fill="#b5121b"/><path d="M2 5l10 8 10-8" fill="none" stroke="#fff" stroke-width="1.6"/></svg>
      dean.vossler@marloweholdingsffl.com
    </li>
    <li>
      <svg viewBox="0 0 24 24" aria-hidden="true"><circle cx="12" cy="12" r="10" fill="#b5121b"/><path d="M2 12h20M12 2c3 3 3 17 0 20M12 2c-3 3-3 17 0 20" fill="none" stroke="#fff" stroke-width="1.4"/></svg>
      www.marloweholdingsffl.com
    </li>
    <li>
      <svg viewBox="0 0 24 24" aria-hidden="true"><rect x="2" y="5" width="20" height="14" rx="2" fill="#b5121b"/><path d="M6 10h6M6 14h9" stroke="#fff" stroke-width="1.6"/></svg>
      KPV FFL: 5-21-xxx-xx-xx-04519
    </li>
  </ul>

  <div class="edge-tab"></div>
</section>

<section class="card card-back">
  <div class="arms-art" role="img" aria-label="Embossed illustration of two crossed rifles"></div>
  <div class="back-brand">
    <span class="dot"></span>
    <p class="name">Marlowe<br>Holdings LLC</p>
  </div>
</section>

</body>
</html>
```